make it look old timey and motherly but mordern...bath soak with cooling vapors. tall pine hush

need a bath soak label...cooling vapors. will be in a pouch like below. dont pay attention to the design, just attatching so you know the kind of pouch itll be in. need something trusty, minimal and clean...its called tall pine hush bath soak the best bath yull ever take.... for sore muscles, cooling vapors, smells good...made with menthol lemon and eucalyptus...give me something good.

Target Market(s)

make it look old timey and motherly but mordern

Font styles to use
Serif
Sans Serif

Colors
0054AA
0677BA
7BADD7
CADEEF
E8F1F8
0094D4
00A9DD
6FCCEA
C7EBF8
E9F6FB
FFF300
FFF600
FEFA6F
FFFEC7
FFFEE8
FFC000
F8CF3A
FAE287
FDF2CF
FEFAEE
E54698
E96AAD
F1A4CE
F9D9EA
FCEFF6
6B429C
8869AF
B7A5CE
E3DAEB
F3F0F8

```html
<!DOCTYPE html>
<html lang="en">
<head>
<meta charset="utf-8">
<title>Tall Pine Hush Bath Soak – Pouch Labels</title>
<link href="https://fonts.googleapis.com/css2?family=Montserrat+Alternates:ital,wght@1,400;1,500&display=swap" rel="stylesheet">
<style>
  :root {
    --backdrop: #e6e6e6;
    --ink: #161616;
    --lemon-pale: #fffec7;
    --lemon-soft: #e4e3a6;
    --lemon-glow: #fcfcc0;
    --sky-soft: #c7ebf8;
    --sky-mid: #6fccea;
    --sky-deep: #5bbcd6;
    --rose-deep: #e6abcb;
    --rose-mid: #f1b8d8;
    --rose-pale: #f9d9ea;
    --rose-mist: #fcedf6;
    --lilac: #d9c2da;
  }
  * { box-sizing: border-box; margin: 0; padding: 0; }
  html, body {
    width: 1200px;
    height: 750px;
    overflow: hidden;
    background: var(--backdrop);
    font-family: "Montserrat Alternates", sans-serif;
    color: var(--ink);
  }
  .canvas { position: relative; width: 1200px; height: 750px; }

  .pouch {
    position: absolute;
    top: 169px;
    width: 256px;
    height: 401px;
    border-radius: 10px 10px 0 0;
    overflow: hidden;
  }
  .pouch--lemon-sky {
    left: 320px;
    background:
      radial-gradient(ellipse 120px 90px at 60% 36%, var(--lemon-glow), transparent 70%),
      linear-gradient(160deg, var(--lemon-soft) 0%, var(--lemon-pale) 38%, var(--sky-soft) 58%, var(--sky-deep) 78%, var(--sky-mid) 100%);
  }
  .pouch--rose {
    left: 608px;
    background:
      radial-gradient(ellipse 110px 120px at 65% 40%, var(--rose-mist), transparent 70%),
      linear-gradient(170deg, var(--rose-deep) 0%, var(--rose-mid) 35%, var(--lilac) 70%, var(--rose-pale) 100%);
  }

  .brand-title {
    position: absolute;
    right: 45px;
    top: 30px;
    text-align: right;
    font-style: italic;
    font-weight: 400;
    font-size: 52px;
    line-height: 52px;
    letter-spacing: -0.5px;
    text-transform: uppercase;
  }
  .brand-title span { display: block; }

  .tagline {
    position: absolute;
    left: 232px;
    top: 280px;
    transform-origin: 0 0;
    transform: rotate(-90deg);
    width: 241px;
    font-style: italic;
    font-size: 14.5px;
    white-space: nowrap;
    line-height: 1;
  }

  .divider {
    position: absolute;
    left: 93px;
    top: 309px;
    width: 136px;
    height: 1.2px;
    background: var(--ink);
  }

  .ingredients {
    position: absolute;
    right: 25px;
    top: 325px;
    text-align: right;
    font-style: italic;
    font-size: 8.6px;
    line-height: 10px;
  }

  .net-weight {
    position: absolute;
    left: 14px;
    top: 365px;
    font-style: italic;
    font-weight: 500;
    font-size: 6.6px;
    line-height: 8px;
  }
</style>
</head>
<body>
<main class="canvas">

  <section class="pouch pouch--lemon-sky" aria-label="Bath soak pouch, lemon and sky">
    <h1 class="brand-title"><span>Tall</span><span>Pine</span><span>Hush</span><span>Bath</span><span>Soak</span></h1>
    <p class="tagline">The best bath you'll ever take</p>
    <div class="divider"></div>
    <p class="ingredients">made with menthol lemon<br>and eucalyptus</p>
    <p class="net-weight">Net Wheight :<br>15 Ounces (425 Grams)</p>
  </section>

  <section class="pouch pouch--rose" aria-label="Bath soak pouch, rose">
    <h1 class="brand-title"><span>Tall</span><span>Pine</span><span>Hush</span><span>Bath</span><span>Soak</span></h1>
    <p class="tagline">The best bath you'll ever take</p>
    <div class="divider"></div>
    <p class="ingredients">made with menthol lemon<br>and eucalyptus</p>
    <p class="net-weight">Net Wheight :<br>15 Ounces (425 Grams)</p>
  </section>

</main>
</body>
</html>
```